Virtual Racing Community for Runners Needs a Refreshed Web Design

We are a STARTUP. The current website consists of 3 main pages that function well; however, they are not producing the proper conversions because we need a more professional look and better execution of our great ideas.

First page: landing page that needs to be intriguing, sleek, create urgency, incorporate our call to action and most importantly get the consumer to click a button to get to second page. www.trelomark.com

Second page: sign up page that incorporates our already existing postwren form that doesn't take the viewer away from the page on incorrect form field entry. On successful completion needs to inform the viewer to check the email and confirm (possibly in spam) and open third page. http://www.trelomark.com/beta.html

Third page: preorder page that allows the user prepurchase through a well working form through "www.usebaskin.com." This interface works really well; however, the graphics and page need to really entice the viewer to buy. http://www.trelomark.com/preorder.html

And that's it!!! Simple 3 pages that function currently 95% how we want it, but really needs that creative touch to push it to the next level!

Contact us with any other questions!
Updates

Reason: I have provided numerous feedback and am awaiting redesigns. Have it narrowed down to 2 designers. Need time to vet with stakeholders.

Industry/Entity Type

Racing

```html
<!DOCTYPE html>
<html lang="en">
<head>
<meta charset="utf-8">
<title>Trelomark – Finish Your Races Proud</title>
<link rel="stylesheet" href="https://fonts.googleapis.com/css2?family=League+Gothic&family=Oswald:wght@400;500&display=swap">
<style>
:root{
  --ink:#000;
  --brown-dark:#5a2c0c;
  --brown-mid:#7b4a1e;
  --brown:#8f5322;
  --orange:#d97b1a;
  --cream:#f7e3b8;
  --footer:#141414;
  --body-text:#444;
  --white:#fff;
}
*{margin:0;padding:0;box-sizing:border-box}
html,body{width:1200px;height:1053px;overflow:hidden;background:var(--white);font-family:Arial,Helvetica,sans-serif}
.page{position:relative;width:1200px;height:1053px}
.hero{position:absolute;left:0;top:0;width:1200px;height:522px;
  background:linear-gradient(180deg,#e9a441 0%,#f0b552 30%,#e08e25 62%,#8a4a16 84%,#2e1a0c 100%)}
.hero-copy{position:absolute;left:605px;top:0}
.brand{position:absolute;left:2px;top:20px;font-family:"League Gothic",sans-serif;font-size:112px;line-height:1;color:var(--ink);letter-spacing:2px}
.headline{position:absolute;left:0;top:138px;white-space:nowrap;font-family:"League Gothic",sans-serif;font-size:60px;line-height:1;color:var(--brown-dark)}
.tagline{position:absolute;left:0;top:195px;white-space:nowrap;font-family:"League Gothic",sans-serif;font-size:44px;line-height:1;color:var(--brown-mid);letter-spacing:1px}
.event-title{position:absolute;left:0;top:280px;white-space:nowrap;font-family:"League Gothic",sans-serif;font-size:46px;line-height:1;color:var(--ink)}
.event-text{position:absolute;left:3px;top:325px;width:370px;font-size:14px;line-height:17px;color:var(--ink)}
.register{position:absolute;left:0;top:375px;display:flex;height:54px;text-decoration:none}
.register .arrow{width:60px;background:var(--ink);display:flex;align-items:center;justify-content:center}
.register .label{width:193px;background:var(--brown);color:var(--cream);font-family:"League Gothic",sans-serif;font-size:36px;display:flex;align-items:center;justify-content:center}
.card{position:absolute;left:110px;top:486px;width:980px;height:320px;background:var(--white);box-shadow:0 10px 22px rgba(0,0,0,.12)}
.latest{display:flex;height:104px}
.date{width:98px;background:var(--orange);color:var(--white);display:flex;flex-direction:column;align-items:center;padding-top:17px}
.date-day{width:44px;height:44px;border:2px solid var(--white);border-radius:50%;display:flex;align-items:center;justify-content:center;font-family:"Oswald",sans-serif;font-size:21px}
.date-month{font-size:14px;margin-top:6px}
.latest-body{flex:1;background:var(--brown);color:var(--white);padding:14px 40px 0 16px}
.latest-body h2{font-weight:normal;font-size:18px;margin-bottom:10px}
.latest-body p{font-size:13px;line-height:16px}
.feature{position:absolute;top:172px;width:260px}
.feature .icon{position:absolute;left:-60px;top:2px}
.feature h3{font-weight:normal;font-size:18px;color:#222;margin-left:-1px}
.feature p{font-size:13px;line-height:15.5px;color:var(--body-text);margin-top:6px;height:54px}
.view{display:flex;height:25px;width:77px;text-decoration:none}
.view span{width:49px;background:var(--brown);color:var(--white);font-size:12px;display:flex;align-items:center;justify-content:center}
.view i{width:28px;background:#111;display:flex;align-items:center;justify-content:center}
.footer{position:absolute;left:0;top:862px;width:1200px;height:128px;background:var(--footer);color:var(--white)}
.connect{position:absolute;left:113px;top:28px;font-family:"League Gothic",sans-serif;font-size:30px;letter-spacing:.5px}
.socials{position:absolute;left:115px;top:71px;display:flex;gap:20px}
.socials span{width:40px;height:40px;border:2px solid var(--white);border-radius:50%}
.contact{position:absolute;left:829px;top:32px;color:#ddd}
.contact-row{display:flex;align-items:center;gap:12px}
.contact-icon{width:32px;height:32px;border:2px solid var(--white);border-radius:50%;display:flex;align-items:center;justify-content:center}
.address{font-size:12px;line-height:18px}
.phone{font-size:24px;color:#ccc;margin-top:10px}
.bottom-bar{position:absolute;left:0;top:990px;width:1200px;height:48px;background:var(--orange);color:var(--white);font-size:11px}
.bottom-bar .copy{position:absolute;left:115px;top:18px}
.bottom-bar .links{position:absolute;right:115px;top:18px}
.base{position:absolute;left:0;top:1038px;width:1200px;height:15px;background:var(--footer)}
</style>
</head>
<body>
<div class="page">
  <section class="hero" role="img" aria-label="Photo of a runner silhouetted against an orange sunset sky"></section>
  <div class="hero-copy">
    <div class="brand">TRELOMARK</div>
    <h1 class="headline">FINISH YOUR RACES PROUD</h1>
    <p class="tagline">AIM. ATTEMPT. ACHIEVE.</p>
    <h2 class="event-title">CHICAGO BETA RUN WEEK 2</h2>
    <p class="event-text">For a limited time be the first to receive early access and receive a Real Life Beta Tester t-shirt.</p>
    <a class="register" href="#">
      <span class="arrow"><svg width="26" height="20" viewBox="0 0 26 20"><path d="M2 10h20M14 2l8 8-8 8" stroke="#fff" stroke-width="3" fill="none"/></svg></span>
      <span class="label">REGISTER NOW</span>
    </a>
  </div>

  <section class="card">
    <div class="latest">
      <div class="date"><div class="date-day">23</div><div class="date-month">AUG</div></div>
      <div class="latest-body">
        <h2>Latest Virtual Run</h2>
        <p>Lorem ipsum dolor sit amet, consectetur adipisicing elit, sed do eiusmod tempor incididunt ut labore et dolore magna aliqua. Ut enim ad minim veniam, quis nostrud exercitation ullamco laboris nisi ut aliquip ex ea commodo consequat.</p>
      </div>
    </div>

    <div class="feature" style="left:85px">
      <svg class="icon" width="42" height="42" viewBox="0 0 42 42"><path d="M11 4h20v10c0 7-4 11-10 11S11 21 11 14z" fill="#333"/><path d="M11 8H5c0 7 3 10 7 10M31 8h6c0 7-3 10-7 10" stroke="#333" stroke-width="3" fill="none"/><rect x="18" y="25" width="6" height="7" fill="#333"/><rect x="12" y="32" width="18" height="6" fill="#333"/></svg>
      <h3>freebies and giveaways</h3>
      <p>Duis aute irure dolor in reprehenderit in voluptate velit esse cillum dolore eu fugiat nulla pariatur.</p>
      <a class="view" href="#"><span>view</span><i><svg width="12" height="10" viewBox="0 0 12 10"><path d="M1 5h9M6 1l4 4-4 4" stroke="#fff" stroke-width="1.6" fill="none"/></svg></i></a>
    </div>

    <div class="feature" style="left:408px">
      <svg class="icon" width="50" height="50" viewBox="0 0 50 50"><circle cx="34" cy="7" r="5" fill="#333"/><path d="M8 16h14l10 2-6 10 8 6M24 18l-8 14H6" stroke="#333" stroke-width="5" fill="none" stroke-linejoin="round"/><path d="M2 34h24M22 34v16" stroke="#333" stroke-width="2" fill="none"/></svg>
      <h3>run at your own pace</h3>
      <p>You can walk, jog, skip or run the distance of your choice. You can complete your race at the gym ...</p>
      <a class="view" href="#"><span>view</span><i><svg width="12" height="10" viewBox="0 0 12 10"><path d="M1 5h9M6 1l4 4-4 4" stroke="#fff" stroke-width="1.6" fill="none"/></svg></i></a>
    </div>

    <div class="feature" style="left:736px">
      <svg class="icon" width="52" height="48" viewBox="0 0 52 48"><g fill="#fff" stroke="#333" stroke-width="3.5"><circle cx="16" cy="12" r="10"/><circle cx="38" cy="22" r="11"/><circle cx="16" cy="34" r="12"/></g><g font-family="Arial" font-weight="bold" fill="#333" text-anchor="middle"><text x="16" y="17" font-size="13">$</text><text x="38" y="27" font-size="14">$</text><text x="16" y="40" font-size="16">$</text></g></svg>
      <h3>discounts</h3>
      <p>If you have 10 or more runners interested in participating in one of our races, please contact us and ...</p>
      <a class="view" href="#"><span>view</span><i><svg width="12" height="10" viewBox="0 0 12 10"><path d="M1 5h9M6 1l4 4-4 4" stroke="#fff" stroke-width="1.6" fill="none"/></svg></i></a>
    </div>
  </section>

  <footer class="footer">
    <h2 class="connect">CONNECT WITH US</h2>
    <div class="socials" aria-label="Social links"><span></span><span></span><span></span><span></span></div>
    <div class="contact">
      <div class="contact-row">
        <span class="contact-icon"><svg width="18" height="16" viewBox="0 0 18 16"><path d="M9 1L1 8h3v7h4v-4h2v4h4V8h3z" fill="#fff"/></svg></span>
        <span class="address">48 Larkfield Road Suite 7<br>Brindleford 402118</span>
      </div>
      <div class="contact-row phone">
        <span class="contact-icon"><svg width="16" height="16" viewBox="0 0 16 16"><path d="M3 1l3 3-2 2c1 2 3 4 5 5l2-2 3 3-2 3C7 15 1 9 1 3z" fill="#fff"/></svg></span>
        <span>055-210-4477</span>
      </div>
    </div>
  </footer>
  <div class="bottom-bar">
    <span class="copy">© Copyright 2014 Trelomark. All Rights Reserved</span>
    <span class="links">Policy | Terms</span>
  </div>
  <div class="base"></div>
</div>
</body>
</html>
```